Taking my business to the next level - going national and need new label design.

To begin, I need a label for my elderberry syrup kit and in the near future, I will need labels for five additional products as well as business cards. My companies name is Tamsel Grove, so named because we strongly believe plants have the power to maintain daily health and to provide healing during times of illness.
The elderberry kit should include the following information:
Logo - I can supply
Organic
Aronia & Elderberry
Power Blend
Syrup Kit
Daily Immunity
Allergy Support
It should be editable for different packages and quantities
This label will need to be: 3" tall by 5" wide

I need a second label for this product that measures 1.5" tall and 5" wide.
The second label should include:
our sustainability commitment statement
From our family to yours
makes 32 oz 105 ml
website address - this should stand out
www.TamselGroveCo.com

I am using a Kraft bag to package my product. It has a window on the front; one label will go above the window and the smaller of the two labels will go below.
I am drawn to the colors green and purple. The final design should communicate fresh, clean, and wellness

Health & wellness community, families

Supplement

• I like the font called KAZYcraie found on GlyphBarn - mentioned just as a sample

a54499
9bcb3c
ffc214

• See project description
Sustainability Commitment: (on the second label)
It is our guarantee to provide you with the highest ethical standards in sourcing quality, organic ingredients that support environmental sustainability in line with our commitment to health and wellness.
• no cartoon looks

```html
<!DOCTYPE html>
<html lang="en">
<head>
<meta charset="utf-8">
<title>Tamsel Grove – Syrup Kit Labels</title>
<link rel="stylesheet" href="https://fonts.googleapis.com/css2?family=Delius&family=Roboto+Condensed:ital,wght@0,400;0,700;1,400&display=swap">
<style>
  :root {
    --purple: #5e1b55;
    --purple-text: #5a1a55;
    --green: #5a9a45;
    --green-text: #4f9a3c;
    --ink: #231f20;
    --paper: #ffffff;
    --stage: #ffffff;
  }
  * { margin: 0; padding: 0; box-sizing: border-box; }
  html, body { width: 1200px; height: 1200px; overflow: hidden; background: var(--stage); }
  .canvas { position: relative; width: 1200px; height: 1200px; }

  .label {
    position: absolute;
    left: 220px;
    width: 773px;
    background: var(--paper);
    box-shadow: 4px 6px 14px rgba(0,0,0,0.28);
    overflow: hidden;
  }
  .label--front { top: 137px; height: 463px; }
  .label--back { top: 824px; height: 232px; }

  .brand {
    position: absolute;
    display: flex;
    align-items: center;
    gap: 14px;
    font-family: "Delius", sans-serif;
    color: var(--ink);
    white-space: nowrap;
  }
  .brand__dot { border-radius: 50%; background: var(--green); flex: none; }
  .label--front .brand { left: 60px; top: 310px; font-size: 40px; }
  .label--front .brand__dot { width: 34px; height: 34px; }
  .label--back .brand { left: 18px; top: 112px; font-size: 26px; gap: 9px; }
  .label--back .brand__dot { width: 22px; height: 22px; }

  .organic-tag {
    position: absolute;
    left: 464px; top: 2px;
    width: 251px; height: 85px;
    background: var(--green);
    color: #fff;
    font-family: "Delius", sans-serif;
    font-size: 50px;
    display: flex; align-items: center; justify-content: center;
    letter-spacing: 1px;
  }
  .product-line {
    position: absolute;
    left: 420px; width: 340px;
    text-align: center;
    font-family: "Delius", sans-serif;
    color: var(--ink);
    white-space: nowrap;
  }
  .product-line--fruit { top: 93px; font-size: 30px; letter-spacing: 1px; }
  .product-line--blend { top: 208px; font-size: 36px; letter-spacing: 1px; }
  .product-line--kit { top: 242px; font-size: 66px; color: var(--purple-text); letter-spacing: 2px; }

  .benefits {
    position: absolute;
    left: 440px; top: 372px;
    display: flex; gap: 6px;
    list-style: none;
    font-family: "Roboto Condensed", sans-serif;
    font-size: 17px;
    color: var(--green-text);
  }
  .benefits li { display: flex; align-items: center; gap: 8px; }
  .benefits li::before {
    content: ""; width: 11px; height: 11px; border-radius: 50%; background: var(--ink);
  }

  .web-band {
    position: absolute;
    left: 0; bottom: 0;
    width: 100%; height: 56px;
    background: var(--purple);
    color: #fff;
    font-family: "Roboto Condensed", sans-serif;
    font-style: italic;
    font-size: 30px;
    display: flex; align-items: center; justify-content: flex-end;
    padding-right: 56px;
  }

  .tagline {
    position: absolute;
    left: 235px; top: 82px;
    font-family: "Roboto Condensed", sans-serif;
    font-size: 23px;
    color: var(--green-text);
  }
  .web-tag {
    position: absolute;
    left: 235px; top: 125px;
    width: 222px; height: 35px;
    background: var(--purple);
    color: #fff;
    font-family: "Roboto Condensed", sans-serif;
    font-style: italic;
    font-size: 20px;
    display: flex; align-items: center; justify-content: center;
  }
  .commitment {
    position: absolute;
    left: 235px; top: 166px;
    width: 520px;
    font-family: "Roboto Condensed", sans-serif;
    color: var(--ink);
  }
  .commitment__title { font-size: 18px; font-weight: 700; color: var(--purple-text); line-height: 1.1; }
  .commitment__body { font-size: 9.3px; line-height: 1.2; margin-top: 1px; }
  .rule-band {
    position: absolute;
    left: 0; bottom: 0;
    width: 100%; height: 16px;
    background: var(--purple);
  }
</style>
</head>
<body>
<main class="canvas">
  <section class="label label--front">
    <div class="brand"><span class="brand__dot"></span><span class="brand__name">Tamsel Grove</span></div>
    <div class="organic-tag">Organic</div>
    <p class="product-line product-line--fruit">Aronia &amp; Elderberry</p>
    <p class="product-line product-line--blend">Power Blend</p>
    <h1 class="product-line product-line--kit">Syrup Kit</h1>
    <ul class="benefits">
      <li>Daily Immunity</li>
      <li>Allergy Support</li>
    </ul>
    <div class="web-band">www.TamselGroveCo.com</div>
  </section>

  <section class="label label--back">
    <div class="brand"><span class="brand__dot"></span><span class="brand__name">Tamsel Grove</span></div>
    <p class="tagline">From our family to yours</p>
    <div class="web-tag">www.TamselGroveCo.com</div>
    <div class="commitment">
      <h2 class="commitment__title">Sustainability Commitment:</h2>
      <p class="commitment__body">It is our guarantee to provide you with the highest ethical standards in sourcing quality, organic ingredients that support environmental sustainability in line with our commitment to health and wellness.</p>
    </div>
    <div class="rule-band"></div>
  </section>
</main>
</body>
</html>
```